Flyer Designer for a Widow and Door Company - loooking for fresh design

We are looking for a flyer designed to advertise our business - we supply and install windows and doors - we are looking for a fresh looking flyer to distribute to drum up business - more information can be found at our website www.brightpanehouse.co.uk - We want a different approach than we currently have - making it vibrant and fresh - you can see the services on the website but its more the graphical design that we are looking for rather than content as the content from the website can be used for each service etc.

Target Market(s)

the general public

Colors

Designer to choose colors to be used in the design.

Requirements
Must have
• vibrant design and images

```html
<!DOCTYPE html>
<html lang="en">
<head>
<meta charset="utf-8">
<title>Bright Pane House – Windows and Doors Flyer</title>
<link href="https://fonts.googleapis.com/css2?family=Montserrat:wght@600;700;800&family=Nunito+Sans:ital,wght@0,400;0,600;1,400&display=swap" rel="stylesheet">
<style>
  :root{
    --blue:#2a6db3;
    --orange:#fbaa36;
    --grey:#6d6e70;
    --text:#3f3f42;
    --page:#ffffff;
    --backdrop:#eeeeee;
    --photo-wall:#e6e9e6;
    --photo-floor:#ddd8cd;
  }
  *{box-sizing:border-box;margin:0;padding:0}
  html,body{width:1200px;height:1000px;overflow:hidden;background:var(--backdrop);font-family:"Nunito Sans",Arial,sans-serif}
  .flyer{position:absolute;left:269px;top:22px;width:672px;height:950px;background:var(--page);overflow:hidden}
  .band{position:absolute}
  .hero-photo{position:absolute;left:0;top:18px;width:340px;height:362px;
    background:linear-gradient(to bottom,var(--photo-wall) 0%,var(--photo-wall) 84%,var(--photo-floor) 86%,var(--photo-floor) 100%);
    -webkit-mask-image:linear-gradient(to right,#000 65%,transparent 100%);mask-image:linear-gradient(to right,#000 65%,transparent 100%)}
  .brand{position:absolute;right:36px;top:50px;text-align:right;color:var(--blue)}
  .brand-name{display:flex;align-items:center;justify-content:flex-end;gap:10px;font-family:"Montserrat",sans-serif;font-weight:800;font-size:25px;letter-spacing:.5px}
  .brand-mark{width:26px;height:26px;background:var(--blue)}
  .brand-tag{font-family:"Montserrat",sans-serif;font-weight:700;font-size:10px;letter-spacing:.6px;margin-top:4px}
  .intro{position:absolute;right:36px;top:155px;text-align:right}
  .intro-lead{font-style:italic;font-size:15px;color:var(--grey)}
  .intro-title{font-family:"Montserrat",sans-serif;font-weight:800;font-size:24px;color:var(--blue);margin-top:1px}
  .benefits{position:absolute;right:49px;top:212px;list-style:none;text-align:right}
  .benefits li{display:flex;align-items:center;justify-content:flex-end;gap:6px;font-size:12px;color:var(--text);height:19.4px}
  .benefits svg{width:14px;height:14px}
  .service{position:absolute;width:276px;height:212px;background:var(--orange);color:#fff;text-align:center;padding:12px 14px 0}
  .service svg{height:48px;display:block;margin:0 auto}
  .service h2{font-family:"Montserrat",sans-serif;font-weight:700;font-size:14px;margin:6px 0 6px}
  .service p{font-size:10.5px;line-height:13.4px;margin-bottom:6px}
  .service.justify p{text-align:justify;text-align-last:center}
  .quote{position:absolute;left:44px;top:846px;width:276px;height:77px;border:1.5px dashed #9a9a9a;border-radius:6px;text-align:center}
  .quote-label{position:absolute;left:50%;top:-12px;transform:translateX(-50%);background:var(--page);padding:0 6px;font-size:19px;color:var(--grey);white-space:nowrap;letter-spacing:.4px}
  .quote-phone{font-family:"Montserrat",sans-serif;font-weight:700;font-size:35px;color:var(--blue);margin-top:12px;line-height:1}
  .quote-email{font-size:11.5px;color:var(--grey);margin-top:6px;display:flex;align-items:center;justify-content:center;gap:5px}
  .badge{position:absolute;background:#d9dde3}
</style>
</head>
<body>
<div class="flyer">
  <svg class="band" style="left:0;top:0" width="672" height="26" viewBox="0 0 672 26">
    <polygon points="0,0 135,0 145,18 0,18" fill="var(--orange)"/>
    <polygon points="124,0 672,0 672,26 138,26" fill="var(--blue)"/>
  </svg>

  <div class="hero-photo" role="img" aria-label="Photo of a pale wooden interior door with glass slits in an empty room with a light floor"></div>

  <div class="brand">
    <div class="brand-name"><span class="brand-mark"></span>BRIGHT PANE HOUSE LTD</div>
    <div class="brand-tag">BESPOKE WINDOWS &amp; DOORS</div>
  </div>

  <div class="intro">
    <p class="intro-lead">Your Suppliers and installers of quality</p>
    <h1 class="intro-title">WINDOWS AND DOORS</h1>
  </div>

  <ul class="benefits">
    <li>Registered Installer<svg viewBox="0 0 14 14"><circle cx="7" cy="7" r="6" fill="none" stroke="var(--orange)" stroke-width="1.3"/><path d="M4 7l2.2 2.3L11.5 2.5" fill="none" stroke="var(--orange)" stroke-width="1.6"/></svg></li>
    <li>Additional Security<svg viewBox="0 0 14 14"><circle cx="7" cy="7" r="6" fill="none" stroke="var(--orange)" stroke-width="1.3"/><path d="M4 7l2.2 2.3L11.5 2.5" fill="none" stroke="var(--orange)" stroke-width="1.6"/></svg></li>
    <li>Rated Energy Efficient<svg viewBox="0 0 14 14"><circle cx="7" cy="7" r="6" fill="none" stroke="var(--orange)" stroke-width="1.3"/><path d="M4 7l2.2 2.3L11.5 2.5" fill="none" stroke="var(--orange)" stroke-width="1.6"/></svg></li>
    <li>Precision Made to Measure<svg viewBox="0 0 14 14"><circle cx="7" cy="7" r="6" fill="none" stroke="var(--orange)" stroke-width="1.3"/><path d="M4 7l2.2 2.3L11.5 2.5" fill="none" stroke="var(--orange)" stroke-width="1.6"/></svg></li>
    <li>Competitive Pricing<svg viewBox="0 0 14 14"><circle cx="7" cy="7" r="6" fill="none" stroke="var(--orange)" stroke-width="1.3"/><path d="M4 7l2.2 2.3L11.5 2.5" fill="none" stroke="var(--orange)" stroke-width="1.6"/></svg></li>
    <li>Friendly Professional Staff<svg viewBox="0 0 14 14"><circle cx="7" cy="7" r="6" fill="none" stroke="var(--orange)" stroke-width="1.3"/><path d="M4 7l2.2 2.3L11.5 2.5" fill="none" stroke="var(--orange)" stroke-width="1.6"/></svg></li>
    <li>No Obligation Quote<svg viewBox="0 0 14 14"><circle cx="7" cy="7" r="6" fill="none" stroke="var(--orange)" stroke-width="1.3"/><path d="M4 7l2.2 2.3L11.5 2.5" fill="none" stroke="var(--orange)" stroke-width="1.6"/></svg></li>
  </ul>

  <section class="service" style="left:43px;top:381px">
    <svg viewBox="0 0 36 48" width="36"><rect x="2" y="2" width="32" height="44" fill="none" stroke="#fff" stroke-width="3"/><path d="M2 24h32M12.7 2v44M23.3 2v44M2 13h32M2 35h32" stroke="#fff" stroke-width="2"/></svg>
    <h2>OUR WINDOWS</h2>
    <p>Our windows are individually designed to suit your home. Bespoke to your individual requirements.</p>
    <p>Our windows offer an excepional level of energy efficency with market leading locking systems.</p>
    <p class="j">With an extensive choice of styles, colours and finishes, do not hesitate in contacting us today to discuss your requirements.</p>
  </section>

  <section class="service justify" style="left:346px;top:381px">
    <svg viewBox="0 0 40 48" width="40"><path d="M6 46V3h28v43" fill="none" stroke="#fff" stroke-width="3"/><polygon points="6,3 22,8 22,46 6,46" fill="#fff"/><circle cx="18" cy="27" r="1.6" fill="var(--orange)"/><path d="M0 46.5h40" stroke="#fff" stroke-width="3"/></svg>
    <h2>OUR DOORS</h2>
    <p>A new door from Bright Pane House can transform the look of your home, offer increased thermal efficiency and dramatically improve security for your peace of mind.</p>
    <p>With literally hundreds of different designs, colours and finishes to choose from, contact us today for a free, no obligation quotation.</p>
  </section>

  <section class="service" style="left:43px;top:614px">
    <svg viewBox="0 0 48 48" width="48"><path d="M8 40L38 10" stroke="#fff" stroke-width="6" stroke-linecap="round"/><circle cx="38" cy="10" r="7" fill="#fff"/><circle cx="42" cy="6" r="3.5" fill="var(--orange)"/><path d="M40 40L14 14" stroke="#fff" stroke-width="5" stroke-linecap="round"/><path d="M8 8l8 2-6 6z" fill="#fff"/></svg>
    <h2>REPAIRS</h2>
    <p>At the Bright Pane House we offer a full repair and replacement service on glass units, windows and doors. No job is too small. Please contact one of our helpful advisors for a non obligatory quotation or to learn more please click the link below.</p>
  </section>

  <section class="service justify" style="left:346px;top:614px">
    <svg viewBox="0 0 48 48" width="48"><path d="M4 20L24 4l20 16v16H18l-9 9v-9H4z" fill="#fff"/><rect x="33" y="5" width="5" height="10" fill="#fff"/></svg>
    <h2>LANDLORD SERVICES</h2>
    <p>We work closely with Landlords &amp; Letting Agents to offer a full repair or replacement service on glass units, windows and doors as well as adjustments and replacement or repair of hinges, handles locks and cylinders. We also offer property surveys and recommendations on the condition of the current windows and doors.</p>
  </section>

  <div class="quote">
    <span class="quote-label">REQUEST A FREE QUOTE</span>
    <div class="quote-phone">01632 960418</div>
    <div class="quote-email"><svg width="12" height="9" viewBox="0 0 12 9"><rect width="12" height="9" fill="var(--grey)"/><path d="M0 0l6 5 6-5" fill="none" stroke="#fff" stroke-width="1"/></svg>sales@brightpanehouse.co.uk</div>
  </div>

  <div class="badge" style="left:362px;top:848px;width:96px;height:20px;border-radius:3px;background:#1f3f73"></div>
  <div class="badge" style="left:485px;top:842px;width:36px;height:36px;border-radius:50%;background:#3c84c4"></div>
  <div class="badge" style="left:562px;top:844px;width:36px;height:30px;border-radius:50%;background:#c9c2c4"></div>
  <div class="badge" style="left:390px;top:880px;width:38px;height:42px;border-radius:3px;background:#c99a33"></div>
  <div class="badge" style="left:460px;top:893px;width:146px;height:20px;border-radius:3px;background:#e23a3a"></div>

  <svg class="band" style="left:0;top:926px" width="672" height="24" viewBox="0 0 672 24">
    <polygon points="530,8 672,8 672,24 530,24" fill="var(--orange)"/>
    <polygon points="0,2 528,2 542,24 0,24" fill="var(--blue)"/>
  </svg>
</div>
</body>
</html>
```